www.harborsearchhq.com RE-DESIGN with SiteForge

We need to update our current site to SiteForge and will also need to add several pages. We will not be very picky on the style and elements as long as the colors and logos are the same-- AL INFO ON SITE WILL STAY THE SAME...CURRENT SITE IS VERY OUTDATED.

The project will consist of using the current site as template (all pics, text etc) and then transferring all the info into a more up to date version. We will also need to add the following functions:

1.) Job Listings page of the current openings our recruitment agency is working on (Must be easily edited and changed) and will allow candidate to submit their resumes via a simple email link)

2.) Featured candidate page that highlights one of our current candidates (profile, pic, editable filed so we may paste bio (must be easily edited via word press.

3.) Bio Page of our current Recruiters (4 bios) - Editable so we can make changes

4.) ALL FINAL FILES MUST BE MIGRATED AND UPLOADED VIA THE DESIGNER SO WE CAN MAKE THE SITE.
Updates

Please make the "homepage" a scrolling page that include all the drop down menu categories using the same info on current site. We can edit or scale back the text if needed. Would, like to see new stock photos and photos must scale to fit all the way across screen and also be mobile and tablet friendly.

Target Market(s)

professional

Coding

Coded - Design and coding required

Font styles to use
Sans Serif

Colors
0355a3
ec1f27
000000
1b1b1b

Requirements
Must have
• All the current info on existing site www.harborsearchhq.com
• Would like to have design with scolling home page such as:
• Did you get earlier message about the design I eliminated? I was hoping for site more like this?
• https://www.brightpathhire.com/
• https://www.netmarvel.com.au/lp/seo-analysis/
Nice to have
• Sleek masculine modern feel
Should not have
• No cursive

```html
<!DOCTYPE html>
<html lang="en">
<head>
<meta charset="utf-8">
<title>Harbor Search Group – Page Layouts</title>
<link rel="stylesheet" href="https://fonts.googleapis.com/css2?family=Encode+Sans+Condensed:wght@300;400;500;600&display=swap">
<style>
:root{
  --blue:#0355a3;
  --red:#ec1f27;
  --black:#000000;
  --ink:#1b1b1b;
  --paper:#f4f4f4;
  --header:#f6f6f6;
  --muted:#555555;
  --label:#2ee0a9;
  --rule:#e2e2e2;
  --link:#6a4bd8;
  --accent:#ffd27a;
}
*{box-sizing:border-box;margin:0;padding:0}
html,body{width:1200px;height:707px;overflow:hidden;background:#ffffff}
body{position:relative;font-family:"Encode Sans Condensed",sans-serif;color:var(--ink)}

.page-number{position:absolute;font-family:"Encode Sans Condensed",sans-serif;font-weight:300;font-size:86px;line-height:1;color:var(--label)}
.page-number--one{left:28px;top:268px}
.page-number--two{left:606px;top:278px}

.site{position:absolute;background:var(--paper);overflow:hidden;box-shadow:0 0 3px rgba(0,0,0,.12)}
.site--faq{left:114px;top:17px;width:432px;height:675px}
.site--about{left:684px;top:20px;width:468px;height:670px}

.site-header{background:var(--header);position:relative}
.site--faq .site-header{height:48px}
.site--about .site-header{height:50px}
.brand{position:absolute;left:42px;top:14px;display:flex;align-items:center;gap:4px}
.brand-dot{width:13px;height:13px;border-radius:50%;background:var(--red)}
.brand-name{font-size:13px;font-weight:500;color:var(--ink);line-height:1}

.main-nav{background:var(--red);height:25px;display:flex;justify-content:center;align-items:center;gap:9px;font-size:5.6px;color:#fff}
.main-nav span.is-active{color:var(--ink)}

.hero{position:relative;display:flex;flex-direction:column;align-items:center;justify-content:center;color:#fff}
.site--faq .hero{height:107px;background:radial-gradient(circle at 30% 40%,#d9d9d9 0%,#9d9d9d 35%,#6e6e6e 70%,#8c8c8c 100%)}
.site--about .hero{height:112px;background:linear-gradient(135deg,#8a4a24 0%,#c77a3e 30%,#e7c9a3 55%,#7a3d1f 80%,#b56a33 100%)}
.hero-kicker{font-size:4.5px;letter-spacing:.5px;margin-bottom:8px}
.hero-title{font-weight:400}
.site--faq .hero-title{font-size:17px}
.site--about .hero-title{font-size:27px;letter-spacing:1px;margin-top:-6px}
.hero-dot{width:5px;height:5px;border-radius:50%;background:#fff;margin-top:16px}

/* FAQ */
.faq{height:314px;padding:12px 42px 0 46px}
.faq-item{border-bottom:1px solid var(--rule);padding:6px 4px;line-height:10px;font-size:7.8px;color:var(--muted);font-weight:400}
.faq-item::before{content:"+";margin-right:4px}
.faq-item.is-open::before{content:"−"}
.faq-answer{font-size:5.3px;line-height:10px;color:var(--ink);padding:7px 0 4px}
.faq-answer p{margin-bottom:6px}
.faq-answer ul{list-style:none;margin:0 0 6px 12px}
.faq-answer li{display:flex;gap:3px;line-height:10.5px}
.faq-answer li::before{content:"";width:2.5px;height:2.5px;border-radius:50%;background:var(--ink);margin-top:4px;flex:none}

/* About */
.about{height:301px;padding:4px 44px 0 42px;font-size:7.3px;line-height:12.9px;color:var(--ink);overflow:hidden}
.about p{margin-bottom:7px}
.about-lead{display:flex;gap:6px}
.dropcap{font-size:62px;line-height:.85;font-weight:300;color:var(--ink);margin-top:2px}
.about ol{list-style:none;font-size:5.9px;line-height:10.5px;margin-left:6px}
.about a{color:var(--link);text-decoration:none}

/* Footer */
.site-footer{background:var(--blue);position:relative;color:#fff}
.site--faq .site-footer{height:152px}
.site--about .site-footer{height:159px}
.footer-col{position:absolute;top:10px;width:88px}
.footer-heading{color:var(--red);font-size:10.5px;line-height:1.05;text-align:center;font-weight:400;height:26px}
.footer-rule{height:1px;background:rgba(255,255,255,.55);margin:3px 0 9px}
.footer-brand{display:flex;align-items:center;gap:2px;font-size:5px;color:#fff;margin:8px 0 18px}
.footer-brand i{width:6px;height:6px;border-radius:50%;background:var(--red);display:block}
.footer-text{font-size:5.4px;line-height:1.5;font-weight:600}
.footer-text .gap{display:block;height:7px}
.footer-text b{color:var(--accent);font-weight:600}
.candidate{display:flex;gap:4px}
.candidate-photo{width:30px;height:30px;background:linear-gradient(#5d5d5d,#8f8f8f);flex:none}
.candidate-name{font-size:8.5px;line-height:1.1}
.candidate-role{font-size:4.8px;margin-top:3px}
.contact-list{margin:6px 0 0 4px;font-size:4.8px;line-height:1.9;list-style:none}
.contact-list li{display:flex;align-items:center;gap:5px}
.contact-list svg{width:5px;height:5px;flex:none}
.contact-list .indent{padding-left:10px;margin-top:4px}
.link-list{list-style:none;font-size:5.5px;line-height:1.75;padding-left:2px}
.site--about .footer-heading{font-size:11px}
.site--about .contact-list{font-size:5px}
.site--about .link-list{font-size:5.6px}

.site-bottom{background:var(--red);display:flex;justify-content:center;align-items:center;font-size:4.8px;color:#fff}
.site--faq .site-bottom{height:25px}
.site--about .site-bottom{height:24px}
.site-bottom em{font-style:normal;color:var(--link)}
</style>
</head>
<body>

<div class="page-number page-number--one">1</div>
<div class="page-number page-number--two">2</div>

<!-- FAQ page -->
<section class="site site--faq">
  <header class="site-header">
    <div class="brand"><span class="brand-dot"></span><span class="brand-name">Harbor</span></div>
  </header>
  <nav class="main-nav">
    <span>HOME</span><span>ABOUT US</span><span>Areas Of Expertise ▾</span><span>GUARENTEE</span><span class="is-active">FAQ</span><span>TESTIMONIALS</span><span>SUBMIT RESUME</span><span>CONTACT US</span><span>JOBS</span>
  </nav>
  <div class="hero" role="img" aria-label="Banner photo of a glowing light bulb in grey tones">
    <div class="hero-kicker">FAQ</div>
    <div class="hero-title">Frequently Asked Questions</div>
    <div class="hero-dot"></div>
  </div>
  <div class="faq">
    <div class="faq-item is-open">Why don't I just use 2-3 contingent firms and let them fight it out?</div>
    <div class="faq-answer">
      <p>Using several firms and having an influx of resumes sounds like an ideal situation, until you consider that fact that most contingent firms will submit and insurmountable amount of resumes in the hopes of having a candidate "stick". This causes the HR department to "bog down" with unqualified resumes and slows the process down considerably as you wade through the pile of resumes and conduct a search within the search. If they don't bury your HR department with resumes your candidate pool usually consist of:</p>
      <ul>
        <li>candidates that are not screened</li>
        <li>candidates that do not have the right qualifications</li>
        <li>candidates that know nothing about the company, culture or opportunity</li>
        <li>candidates that more than likely are out of work or looking for other employment</li>
        <li>candidates recruited off job boards or ads (not top performers!)</li>
      </ul>
      <p>Having one resource with whom you are in contact and having one reference of communication can speed a search by weeks or even months! Using several contingent firms will require 2-3 times the effort, scheduling, communication and frustration.</p>
    </div>
    <div class="faq-item">Is there really a difference in candidates provided between contingent and retained firms?</div>
    <div class="faq-item">Aren't retained searches are too expensive?</div>
    <div class="faq-item">Why should I engage in a retained agreement?</div>
    <div class="faq-item">How am I sure Harbor Search Group provide the right candidate?</div>
    <div class="faq-item">What if the candidate provided leaves our employment?</div>
    <div class="faq-item">What is my initial investment and do you have other fee structures?</div>
  </div>
  <footer class="site-footer">
    <div class="footer-col" style="left:38px">
      <div class="footer-heading">CONTACT US</div>
      <div class="footer-rule"></div>
      <div class="footer-brand"><i></i>Harbor</div>
      <div class="footer-text">48 Linden Ave.<span class="gap"></span>Harbor City, FL 30412<span class="gap"></span><i>Phone:</i> 555-014-2290<br><i>Email:</i> <b>info@harborsearchhq.com</b></div>
    </div>
    <div class="footer-col" style="left:136px">
      <div class="footer-heading">FEATURED<br>CANDIDATE</div>
      <div class="footer-rule"></div>
      <div class="candidate">
        <div class="candidate-photo" role="img" aria-label="Portrait photo of the featured candidate"></div>
        <div><div class="candidate-name">Marcus Hale</div><div class="candidate-role">Web Developer</div></div>
      </div>
      <ul class="contact-list">
        <li><svg viewBox="0 0 10 10"><rect x="1" y="2" width="8" height="6" fill="none" stroke="#fff"/><path d="M1 2l4 3 4-3" fill="none" stroke="#fff"/></svg>info@harborsearchhq.com</li>
        <li><svg viewBox="0 0 10 10"><path d="M2 1l2 2-1 1.5c1 1.5 1.5 2 3 3L7.5 6l2 2-1.5 1.5C4 9 1 6 .5 2.5z" fill="#fff"/></svg>555-014-2290</li>
        <li><svg viewBox="0 0 10 10"><circle cx="5" cy="5" r="4" fill="none" stroke="#fff"/><path d="M1 5h8M5 1v8" stroke="#fff"/></svg>www.harborsearchhq.com</li>
        <li style="margin-top:4px"><svg viewBox="0 0 10 10"><path d="M5 9.5C2 6 2 5 2 4a3 3 0 016 0c0 1 0 2-3 5.5z" fill="none" stroke="#fff"/></svg>48 Linden Ave.</li>
        <li class="indent">Harbor City, FL 30412</li>
      </ul>
    </div>
    <div class="footer-col" style="left:233px;width:80px">
      <div class="footer-heading">AREAS OF<br>EXPERTISE</div>
      <div class="footer-rule"></div>
      <ul class="link-list"><li>Therapeutic Areas</li><li>Healthcare Marketing</li><li>Biotech</li><li>Medical Devise</li><li>Pharmaceuticals</li><li>Executive Level Management</li><li>Sales Force Expansion</li><li>Sales And Marketing</li></ul>
    </div>
    <div class="footer-col" style="left:318px">
      <div class="footer-heading">MENU</div>
      <div class="footer-rule"></div>
      <ul class="link-list"><li>HOME</li><li>ABOUT US</li><li>FAQ</li><li>GUARENTEE</li><li>SUBMIT RESUME</li><li>TESTIMONIALS</li><li>JOBS</li><li>POST A JOB</li></ul>
    </div>
  </footer>
  <div class="site-bottom"><em>Proudly powered by SiteForge</em>&nbsp;| Theme: HarborSearch by&nbsp;<em>Northlane</em>&nbsp;(Version: 1.0)</div>
</section>

<!-- About page -->
<section class="site site--about">
  <header class="site-header">
    <div class="brand" style="left:46px;top:15px"><span class="brand-dot"></span><span class="brand-name">Harbor</span></div>
  </header>
  <nav class="main-nav" style="font-size:5.9px;gap:10px">
    <span>HOME</span><span class="is-active">ABOUT US</span><span>Areas Of Expertise ▾</span><span>GUARENTEE</span><span>FAQ</span><span>TESTIMONIALS</span><span>SUBMIT RESUME</span><span>CONTACT US</span><span>JOBS</span>
  </nav>
  <div class="hero" role="img" aria-label="Banner photo of a team working around an office desk in warm tones">
    <div class="hero-title">ABOUT US</div>
    <div class="hero-dot" style="margin-top:12px"></div>
  </div>
  <div class="about">
    <div class="about-lead"><span class="dropcap">H</span><p style="margin-top:0">arbor Search Group is dedicated to, and focused on, helping you secure the most talented people in the market. We assess, recruit, develop and engage the best and brightest people for our corporate clients. Our goal is to improve performance at every level within our client companies so that the whole becomes greater than the sum of each individual's expertise.</p></div>
    <p>Our recruiters have over 75 years of combined recruiting expertise in a wide variety of industries ranging from Sales and Marketing to Clinical Research. This collective industry experience has, over the years, produced invaluable contacts with industry leaders and decision makers across all the business arenas we serve.</p>
    <p>Because of this experience and knowledge, our recruiters are current with the trends and trendsetters around the world, thus, giving our clients a continuous competitive edge.</p>
    <p>We believe that the true test and watermark of a long-term successful agency is to provide only those rare, hard to find, select candidates within an established timeline. Our search philosophy is to absorb as much about your organization as possible and represent your company with the highest of moral and business values while "surgically extracting" the best possible candidates from your competition and the marketplace.</p>
    <p>We pride ourselves with the abilities to:</p>
    <ol>
      <li>1. form long-term partnerships with our clients;</li>
      <li>2. fully understand our clients' business strategies and corporate culture;</li>
      <li>3. forecast sudden changes within the market to effectively deliver the best possible candidates before they begin their job search;</li>
      <li>4. conduct our business with the highest level of integrity and professionalism;</li>
      <li>5. identify the best talent available in the very shortest period of time</li>
      <li>6. take responsibility and accountability for every search we conduct and deliver the exact match within a pre-determined time frame;</li>
      <li>7. offer the only <a>No Risk Guarantee</a> on all retained searches in the recruitment industry;</li>
    </ol>
  </div>
  <footer class="site-footer">
    <div class="footer-col" style="left:42px;width:94px">
      <div class="footer-heading">CONTACT US</div>
      <div class="footer-rule"></div>
      <div class="footer-brand"><i></i>Harbor</div>
      <div class="footer-text">48 Linden Ave.<span class="gap"></span>Harbor City, FL 30412<span class="gap"></span><i>Phone:</i> 555-014-2290<br><i>Email:</i> <b>info@harborsearchhq.com</b></div>
    </div>
    <div class="footer-col" style="left:140px;width:94px">
      <div class="footer-heading">FEATURED<br>CANDIDATE</div>
      <div class="footer-rule"></div>
      <div class="candidate">
        <div class="candidate-photo" role="img" aria-label="Portrait photo of the featured candidate"></div>
        <div><div class="candidate-name">Marcus Hale</div><div class="candidate-role">Web Developer</div></div>
      </div>
      <ul class="contact-list">
        <li><svg viewBox="0 0 10 10"><rect x="1" y="2" width="8" height="6" fill="none" stroke="#fff"/><path d="M1 2l4 3 4-3" fill="none" stroke="#fff"/></svg>info@harborsearchhq.com</li>
        <li><svg viewBox="0 0 10 10"><path d="M2 1l2 2-1 1.5c1 1.5 1.5 2 3 3L7.5 6l2 2-1.5 1.5C4 9 1 6 .5 2.5z" fill="#fff"/></svg>555-014-2290</li>
        <li><svg viewBox="0 0 10 10"><circle cx="5" cy="5" r="4" fill="none" stroke="#fff"/><path d="M1 5h8M5 1v8" stroke="#fff"/></svg>www.harborsearchhq.com</li>
        <li style="margin-top:4px"><svg viewBox="0 0 10 10"><path d="M5 9.5C2 6 2 5 2 4a3 3 0 016 0c0 1 0 2-3 5.5z" fill="none" stroke="#fff"/></svg>48 Linden Ave.</li>
        <li class="indent">Harbor City, FL 30412</li>
      </ul>
    </div>
    <div class="footer-col" style="left:239px;width:92px">
      <div class="footer-heading">AREAS OF<br>EXPERTISE</div>
      <div class="footer-rule"></div>
      <ul class="link-list"><li>Therapeutic Areas</li><li>Healthcare Marketing</li><li>Biotech</li><li>Medical Devise</li><li>Pharmaceuticals</li><li>Executive Level Management</li><li>Sales Force Expansion</li><li>Sales And Marketing</li></ul>
    </div>
    <div class="footer-col" style="left:337px;width:94px">
      <div class="footer-heading">MENU</div>
      <div class="footer-rule"></div>
      <ul class="link-list"><li>HOME</li><li>ABOUT US</li><li>FAQ</li><li>GUARENTEE</li><li>SUBMIT RESUME</li><li>TESTIMONIALS</li><li>JOBS</li><li>POST A JOB</li></ul>
    </div>
  </footer>
  <div class="site-bottom"><em>Proudly powered by SiteForge</em>&nbsp;| Theme: HarborSearch by&nbsp;<em>Northlane</em>&nbsp;(Version: 1.0)</div>
</section>

</body>
</html>
```